依頼詳細
平成26年     開業しましたが、平成27年1月より院の認知度アップ、新規患者様獲得の為
合計で2万枚程度を複数回に分けて新聞折込チラシを行います。
A4サイズでのチラシデザイン制作をお願いいたします。
現在制作中のホームページへの誘導を促したいのでURL入力のスペース確保や、『鈴風台接骨院で検索』などの記載をお願いします。
URLは12月12日現在決定していない為、仮のURLでのデザイン作成をお願いいたします。

シンプルながらも手に取った方の印象に残るような折込チラシデザインをお願いいたします。
記載項目
添付資料内のロゴ・HPサンプル等をご参照いただき、院名/住所/連絡先/受付時間/地図等の記載をお願いいたします。
サイズ
A4
ページ数
片面
希望イメージ
シンプル 複雑
単色 カラフル
暗い 明るい
日常 高級
遊び心 厳粛
未来的 伝統的
女性的 男性的
希望する色
納品ファイル
• 高解像度JPG (.jpg)
• イラストレーター形式 (.ai)
補足説明
ホームページURLはわかり次第ご連絡いたします。

この度はご提案いただきまして誠にありがとうございます。
納品までスムーズにご対応いただき、感謝いたします。
またの機会がございましたらよろしくお願いいたします。

納品までスムーズにご対応いただき、感謝いたします。

短い期間にもかかわらずたくさんのご提案いただき驚いております。

```html
<!DOCTYPE html>
<html lang="ja">
<head>
<meta charset="utf-8">
<title>鈴風台接骨院 チラシ</title>
<link href="https://fonts.googleapis.com/css2?family=Noto+Serif+JP:wght@600;800&family=Noto+Sans+JP:wght@400;500;700&display=swap" rel="stylesheet">
<style>
:root{
  --ink:#2f2f3a;
  --navy:#2b3a55;
  --grey:#6b6b72;
  --hero-light:#d9d6d1;
  --hero-mid:#9a9890;
  --hero-shirt:#6f7552;
  --orange:#f0923b;
  --green:#7dbb4a;
  --blue:#4aa3d6;
  --pink:#e66f9d;
  --purple:#8b6bb8;
  --yellow:#e8c13a;
  --line:#cfcfd4;
  --paper:#ffffff;
}
*{margin:0;padding:0;box-sizing:border-box}
html,body{width:849px;height:1200px;overflow:hidden;background:var(--paper)}
body{position:relative;font-family:"Noto Sans JP",sans-serif;color:var(--ink)}
.abs{position:absolute}
.brand-mark{left:24px;top:24px;width:60px;height:60px;border-radius:50%;border:6px solid var(--green)}
.brand-name{left:0;width:849px;top:22px;text-align:center;font-family:"Noto Serif JP",serif;font-weight:800;font-size:50px;line-height:1.2;letter-spacing:6px;color:var(--navy)}
.tagline{right:40px;top:24px;font-family:"Noto Serif JP",serif;font-size:13px;color:var(--grey);letter-spacing:2px}
.lead{left:0;width:849px;top:96px;text-align:center;font-family:"Noto Serif JP",serif;font-weight:600;font-size:21px;color:var(--ink)}
.hero{left:0;top:141px;width:849px;height:459px;
  background:radial-gradient(ellipse 55% 70% at 48% 62%,var(--hero-shirt),transparent 70%),linear-gradient(180deg,var(--hero-light),var(--hero-mid))}
.hero-band{left:0;top:352px;width:750px;height:52px;background:rgba(255,255,255,.85)}
.hero-copy{left:36px;top:356px;font-family:"Noto Serif JP",serif;font-weight:800;font-size:33px;line-height:1.3;color:var(--ink);letter-spacing:1px}
.symptoms{left:28px;top:504px;display:flex;gap:12px}
.symptom{width:100px;height:76px;color:#fff;font-size:11px;line-height:1.45;display:flex;align-items:center;justify-content:center;text-align:center;padding:4px}
.s1{background:var(--orange)}.s2{background:var(--green)}.s3{background:var(--blue)}.s4{background:var(--pink)}.s5{background:var(--purple)}.s6{background:var(--yellow)}
.h2{font-weight:700;font-size:15px;line-height:1.3;color:var(--navy);border-left:5px solid var(--green);padding-left:8px}
.flow{left:28px;top:656px;display:flex;align-items:center;gap:6px;font-size:11px}
.chip{padding:3px 8px;color:#fff;border-radius:3px}
.arrow{color:var(--grey)}
.para{left:28px;top:690px;width:390px;font-size:10.5px;line-height:1.7;color:var(--grey)}
.menu-title{left:28px;top:812px;font-family:"Noto Serif JP",serif;font-weight:800;font-size:19px;line-height:1.3;color:var(--ink)}
.menu{left:32px;top:844px;list-style:none;font-size:10.5px;line-height:1.6}
.menu li::before{content:"●";color:var(--orange);margin-right:5px;font-size:9px}
.shot{top:622px;height:86px;background:linear-gradient(135deg,#ece6df,#b9b2ab)}
.hours{left:440px;top:746px;border-collapse:collapse;font-size:10.5px;width:380px}
.hours th,.hours td{border-bottom:1px solid var(--line);padding:3px 2px;text-align:center;font-weight:400}
.hours th:first-child,.hours td:first-child{text-align:left;width:120px}
.access{left:440px;top:858px;width:380px;font-size:10.5px;line-height:1.7}
.access .addr{font-weight:700;font-size:12.5px;color:var(--navy);margin-bottom:2px}
.search{left:440px;top:1030px;width:380px;padding:9px;border:2px solid var(--green);text-align:center;font-weight:700;font-size:16px;color:var(--navy)}
.url{left:440px;top:1082px;width:380px;text-align:center;font-size:11px;color:var(--grey)}
.map-title{left:28px;top:970px;font-family:"Noto Serif JP",serif;font-weight:800;font-size:20px;line-height:1.2;color:var(--navy)}
.map{left:28px;top:1000px;width:380px;height:168px;background:linear-gradient(135deg,#f4f4f2,#e2e2de);border:1px solid var(--line)}
</style>
</head>
<body>

<div class="abs brand-mark"></div>
<div class="abs tagline">痛みを癒し　人を助ける</div>
<div class="abs brand-name">鈴風台接骨院</div>
<div class="abs lead">確かな知識、確かな施術であなたの痛みを取り除きます</div>

<div class="abs hero" role="img" aria-label="緑のシャツの男性が腰に手を当てて痛みを訴える写真"></div>
<div class="abs hero-band"></div>
<div class="abs hero-copy">痛みや不調で困っていませんか？</div>

<div class="abs symptoms">
  <div class="symptom s1">腰の痛み・<br>ぎっくり腰</div>
  <div class="symptom s2">首・肩の<br>こり・痛み</div>
  <div class="symptom s3">ひざの<br>痛み</div>
  <div class="symptom s4">スポーツ<br>によるケガ</div>
  <div class="symptom s5">交通事故<br>のケガ</div>
  <div class="symptom s6">捻挫・<br>打撲</div>
</div>

<div class="abs h2" style="left:28px;top:626px">治療の流れ</div>
<div class="abs flow">
  <span class="chip" style="background:var(--orange)">問診</span><span class="arrow">▶</span>
  <span class="chip" style="background:var(--purple)">検査</span><span class="arrow">▶</span>
  <span class="chip" style="background:var(--green)">施術</span><span class="arrow">▶</span>
  <span class="chip" style="background:var(--blue)">自宅での注意</span><span class="arrow">▶</span>
  <span class="chip" style="background:var(--pink)">説明</span>
</div>
<p class="abs para">ケガの原因と状態を丁寧にお聞きし、一人ひとりに合わせた施術を行います。施術後はご自宅での過ごし方もご説明いたします。健康保険が使える場合もございますので、お気軽にご相談ください。</p>

<div class="abs menu-title">各種実費メニューもご用意しております</div>
<ul class="abs menu">
  <li>コンディショニング整体 30分 3,000円</li>
  <li>スペシャルコンディショニング 60分 5,000円</li>
  <li>骨盤・背骨調整 1回 3,000円</li>
  <li>鍼灸施術 1回 3,500円</li>
  <li>テーピング 1回 500円〜</li>
  <li>姿勢改善コンディショニング 1回 4,000円</li>
  <li>スポーツコンディショニング 1回 3,000円</li>
</ul>

<div class="abs shot" style="left:440px;width:186px" role="img" aria-label="院内での施術風景の写真"></div>
<div class="abs shot" style="left:634px;width:186px" role="img" aria-label="ストレッチ指導の写真"></div>

<div class="abs h2" style="left:440px;top:720px">受付時間</div>
<table class="abs hours">
  <tr><th></th><th>月</th><th>火</th><th>水</th><th>木</th><th>金</th><th>土</th><th>日</th></tr>
  <tr><td>9:00〜12:00</td><td>●</td><td>●</td><td>●</td><td>●</td><td>●</td><td>●</td><td>／</td></tr>
  <tr><td>15:00〜20:00</td><td>●</td><td>●</td><td>●</td><td>／</td><td>●</td><td>▲</td><td>／</td></tr>
</table>

<div class="abs h2" style="left:440px;top:830px">アクセス</div>
<div class="abs access">
  <p class="addr">名古屋市東区鈴風台1-2-3 サンライズ鈴風台1F</p>
  <p>地下鉄 鈴風台駅 2番出口より徒歩3分</p>
  <p>駐車場：院前に2台あり</p>
  <p>TEL 052-000-1234　Fax 052-000-1235</p>
  <p>Mobile 090-0000-5678</p>
  <p>Mail info@suzukazedai-sekkotsu.example</p>
  <p>facebook.com/suzukazedai.sekkotsu</p>
</div>

<div class="abs search">『鈴風台接骨院で検索』</div>
<div class="abs url">www.suzukazedai-sekkotsu.example</div>

<div class="abs map-title">MAP</div>
<div class="abs map" role="img" aria-label="鈴風台駅から鈴風台接骨院までの周辺地図"></div>

</body>
</html>
```